Business Card Design Project

"Pine Ledger Systems" is database management company working in the direct marketing & digital printing industries. Currently going through a name & rebranding process we require a new company business card.

Industry/Entity Type

Marketing

```html
<!DOCTYPE html>
<html lang="en">
<head>
<meta charset="utf-8">
<title>Pine Ledger Systems – Business Card</title>
<link rel="stylesheet" href="https://fonts.googleapis.com/css2?family=Ubuntu:wght@300;400;500;700&display=swap">
<style>
  :root {
    --backdrop: #4a4a4a;
    --card-white: #fbfbfb;
    --card-white-edge: #e6e6e6;
    --brand-blue: #2b8fd6;
    --back-top: #1f8fd8;
    --back-bottom: #3fb0ee;
    --back-text: #e9f5fd;
    --back-label: #ffffff;
  }
  * { box-sizing: border-box; margin: 0; padding: 0; }
  html, body {
    width: 1200px;
    height: 900px;
    overflow: hidden;
    background: var(--backdrop);
    font-family: "Ubuntu", sans-serif;
  }
  .canvas {
    position: relative;
    width: 1200px;
    height: 900px;
    display: flex;
    flex-direction: column;
    align-items: center;
    justify-content: center;
    gap: 56px;
  }
  .card {
    width: 620px;
    height: 354px;
    border-radius: 28px;
    position: relative;
    box-shadow: 0 18px 40px rgba(0, 0, 0, 0.35);
  }
  .card-front {
    background: linear-gradient(160deg, var(--card-white) 55%, var(--card-white-edge));
    display: flex;
    align-items: center;
    justify-content: center;
    gap: 18px;
  }
  .brand-dot {
    width: 30px;
    height: 30px;
    border-radius: 50%;
    background: var(--brand-blue);
  }
  .brand-name {
    font-size: 40px;
    font-weight: 500;
    color: var(--brand-blue);
    letter-spacing: 0.5px;
  }
  .card-back {
    background: linear-gradient(180deg, var(--back-top), var(--back-bottom));
    color: var(--back-text);
    padding: 0 40px 38px 40px;
    display: flex;
    flex-direction: column;
    justify-content: flex-end;
  }
  .holder-name {
    font-size: 24px;
    font-weight: 300;
    letter-spacing: 1px;
    text-transform: uppercase;
    color: var(--back-label);
    margin-left: 24px;
  }
  .holder-role {
    font-size: 14px;
    font-weight: 300;
    letter-spacing: 0.8px;
    text-transform: uppercase;
    margin-left: 12px;
    margin-bottom: 16px;
  }
  .contact-line {
    font-size: 16px;
    font-weight: 300;
    line-height: 1.45;
  }
  .contact-line b {
    font-weight: 700;
    color: var(--back-label);
  }
  .address {
    font-size: 16px;
    font-weight: 300;
    margin-top: 14px;
  }
</style>
</head>
<body>
<main class="canvas">
  <section class="card card-front">
    <span class="brand-dot"></span>
    <span class="brand-name">Pine Ledger Systems</span>
  </section>

  <section class="card card-back">
    <p class="holder-name">Nadia Forsythe</p>
    <p class="holder-role">Operation Manager</p>
    <p class="contact-line"><b>Phone</b>: (221) 33 614 20 58 | <b>Fax</b>: (221) 77 402 18 36</p>
    <p class="contact-line"><b>Mail</b>: name@pineledger.com | <b>Web</b>: www.pineledger.com</p>
    <p class="address">Rue des Tamariniers - Plateau, BP 218 - City, Country</p>
  </section>
</main>
</body>
</html>
```